Business Card and Stationery for Brokerage & Consulting Co.
Amber Ridge Associates, Brokerage & Consulting for the Baking Industry
Business Card and Stationery for Brokerage & Consulting Co. - Food
Creative Brief
Professional
Derek Halvorsen
Partner / Business Development
4219 W. Birchmont Ave. Long Beach, CA 90714
derek@amberridgeassociates.com

```html
<!DOCTYPE html>
<html lang="en">
<head>
<meta charset="utf-8">
<title>Amber Ridge Associates — Business Card</title>
<link rel="stylesheet" href="https://fonts.googleapis.com/css2?family=Open+Sans:wght@400;600&display=swap">
<style>
  :root {
    --maroon: #5b1f2c;
    --maroon-dark: #4a1823;
    --olive: #5f6f35;
    --olive-light: #8a9a55;
    --paper: #ffffff;
    --paper-shade: #eeeeee;
    --ink-light: #f3e9eb;
    --backdrop: #e9e9e9;
  }
  * { margin: 0; padding: 0; box-sizing: border-box; }
  html, body {
    width: 1200px; height: 991px; overflow: hidden;
    background: var(--backdrop);
    font-family: "Open Sans", Arial, sans-serif;
  }
  .canvas { position: relative; width: 1200px; height: 991px; }
  .card {
    position: absolute; left: 210px; width: 780px; height: 446px;
    border-radius: 22px; overflow: hidden;
    background: linear-gradient(160deg, var(--paper) 40%, var(--paper-shade) 100%);
    box-shadow: 0 6px 18px rgba(0,0,0,0.18);
  }
  .card--front { top: 30px; }
  .card--back { top: 515px; }
  .card svg.card-shapes { position: absolute; inset: 0; width: 100%; height: 100%; }

  .brand {
    position: absolute; display: flex; align-items: center; gap: 14px;
    color: var(--olive); font-weight: 600; white-space: nowrap;
  }
  .brand__dot { width: 38px; height: 38px; border-radius: 50%; background: var(--maroon); flex: none; }
  .card--front .brand { left: 50%; top: 50%; transform: translate(-50%, -50%); font-size: 34px; }
  .card--front .brand__dot { width: 46px; height: 46px; }
  .card--back .brand { left: 300px; top: 232px; font-size: 26px; }

  .contact-list {
    position: absolute; left: 34px; top: 24px; list-style: none;
    color: var(--ink-light); font-size: 13px; line-height: 21px;
  }
  .contact-list li { display: flex; align-items: center; gap: 9px; }
  .contact-list svg { width: 14px; height: 14px; flex: none; }

  .person {
    position: absolute; right: 40px; bottom: 30px; text-align: right; color: var(--ink-light);
  }
  .person__name { font-size: 16px; font-weight: 600; }
  .person__title { font-size: 12px; margin-top: 2px; }
</style>
</head>
<body>
<main class="canvas">

  <section class="card card--front" aria-label="Card front">
    <div class="brand"><span class="brand__dot"></span>Amber Ridge Associates</div>
  </section>

  <section class="card card--back" aria-label="Card back">
    <svg class="card-shapes" viewBox="0 0 780 446" preserveAspectRatio="none" aria-hidden="true">
      <path d="M0 0 H780 V20 C560 80 300 200 0 235 Z" fill="var(--maroon)"/>
      <path d="M0 235 C300 200 560 80 780 20 V34 C560 96 300 216 0 250 Z" fill="var(--olive)"/>
      <path d="M0 360 C260 335 520 322 780 272 V292 C520 340 260 355 0 377 Z" fill="var(--olive-light)"/>
      <path d="M0 377 C260 355 520 340 780 292 V446 H0 Z" fill="var(--maroon)"/>
    </svg>

    <ul class="contact-list">
      <li><svg viewBox="0 0 14 14"><circle cx="7" cy="7" r="7" fill="var(--ink-light)"/><path d="M7 3a2.4 2.4 0 0 0-2.4 2.4C4.6 7.4 7 11 7 11s2.4-3.6 2.4-5.6A2.4 2.4 0 0 0 7 3z" fill="var(--maroon)"/></svg>4219 W. Birchmont Ave. Long Beach,</li>
      <li><svg viewBox="0 0 14 14"><circle cx="7" cy="7" r="7" fill="none"/></svg>CA 90714</li>
      <li><svg viewBox="0 0 14 14"><circle cx="7" cy="7" r="7" fill="var(--ink-light)"/><path d="M4.5 3.5l1.6-.3.8 1.9-1 .7a5 5 0 0 0 2.3 2.3l.7-1 1.9.8-.3 1.6C7.6 9.6 4.4 6.4 4.5 3.5z" fill="var(--maroon)"/></svg>310 555 0142</li>
      <li><svg viewBox="0 0 14 14"><circle cx="7" cy="7" r="7" fill="var(--ink-light)"/></svg>marcov47</li>
      <li><svg viewBox="0 0 14 14"><circle cx="7" cy="7" r="7" fill="var(--ink-light)"/><rect x="3.5" y="4.5" width="7" height="5" fill="none" stroke="var(--maroon)" stroke-width="1"/><path d="M3.5 4.5L7 7.3l3.5-2.8" fill="none" stroke="var(--maroon)" stroke-width="1"/></svg>derek@amberridgeassociates.com</li>
      <li><svg viewBox="0 0 14 14"><circle cx="7" cy="7" r="7" fill="var(--ink-light)"/><circle cx="7" cy="7" r="3.6" fill="none" stroke="var(--maroon)" stroke-width="1"/><path d="M3.4 7h7.2M7 3.4v7.2" stroke="var(--maroon)" stroke-width="0.8"/></svg>www.amberridgeassociates.com</li>
    </ul>

    <div class="brand"><span class="brand__dot"></span>Amber Ridge Associates</div>

    <div class="person">
      <p class="person__name">Derek Halvorsen</p>
      <p class="person__title">Partner / Business Development</p>
    </div>
  </section>

</main>
</body>
</html>
```